Business Card Design for a Personal Trainer

I need a business card design for my job as a personal trainer. It should have a unique, modern and exclusive design. On the front there should be only my logo with my name and my job. 0163/2918374 Tobias Kellinger Lindenfeldweg 14 80412 Munich Germany The most important contact information is the web adress. it can be bigger than the rest, but its not necessary. The card should be 8,5cmx5,5cm big. Font: Roboto. Colors: black, white, gray, 56c1ff.

```html
<!DOCTYPE html>
<html lang="de">
<head>
<meta charset="utf-8">
<title>Tobias Kellinger – Visitenkarte</title>
<link rel="stylesheet" href="https://fonts.googleapis.com/css2?family=Roboto:wght@400;500;700&display=swap">
<style>
  :root {
    --brand-blue: #5cb6e2;
    --card-white: #efefef;
    --photo-column: #f6f6f6;
    --ink: #1a1a1a;
    --stage: #e4e8b4;
    --white: #ffffff;
  }
  * { margin: 0; padding: 0; box-sizing: border-box; }
  html, body {
    width: 1200px; height: 960px; overflow: hidden;
    background: var(--stage);
    font-family: "Roboto", Arial, sans-serif;
  }
  .canvas {
    position: relative; width: 1200px; height: 960px;
    display: flex; align-items: center; justify-content: center; gap: 60px;
  }
  .card {
    position: relative; width: 510px; height: 330px; overflow: hidden;
    border-radius: 4px;
    box-shadow: 0 6px 18px rgba(0,0,0,0.12);
  }

  /* Front side */
  .card-front {
    background: var(--brand-blue);
    display: flex; flex-direction: column; align-items: center; justify-content: center;
    color: var(--white);
  }
  .wordmark {
    display: flex; align-items: center; gap: 16px;
  }
  .wordmark-square {
    width: 34px; height: 34px; background: var(--white);
  }
  .wordmark-name {
    font-size: 40px; font-weight: 400; letter-spacing: 1px; text-transform: uppercase;
  }
  .job-title {
    margin-top: 14px; display: flex; align-items: center; gap: 12px;
    font-size: 14px; letter-spacing: 6px; text-transform: uppercase;
  }
  .job-title::before {
    content: ""; width: 60px; height: 1px; background: var(--white);
  }

  /* Back side */
  .card-back { background: var(--card-white); }
  .photo-column {
    position: absolute; left: 0; top: 0; width: 165px; height: 270px;
    background: var(--photo-column);
  }
  .portrait {
    position: absolute; left: 22px; top: 18px; width: 180px; height: 252px;
    background: linear-gradient(180deg, #8a8a8a 0%, #3a3a3a 45%, #262626 100%);
    border-radius: 60px 60px 0 0;
  }
  .contact {
    position: absolute; left: 240px; top: 40px; color: var(--ink);
  }
  .contact-name {
    font-size: 22px; font-weight: 500; margin-bottom: 14px;
  }
  .contact-list { list-style: none; font-size: 17px; line-height: 1.3; }
  .contact-list li { display: flex; align-items: flex-start; gap: 8px; }
  .contact-list svg { width: 18px; height: 18px; margin-top: 2px; flex: none; fill: var(--brand-blue); }
  .contact-list .address-line { padding-left: 0; }
  .footer-band {
    position: absolute; left: 0; bottom: 0; width: 100%; height: 60px;
    background: var(--brand-blue); color: var(--white);
    display: flex; align-items: center; justify-content: space-between;
    padding: 0 22px;
  }
  .website { display: flex; align-items: center; gap: 10px; font-size: 17px; }
  .website svg { width: 24px; height: 22px; }
  .band-wordmark { display: flex; align-items: center; gap: 6px; font-size: 12px; text-transform: uppercase; letter-spacing: .5px; }
  .band-wordmark span.square { width: 10px; height: 10px; background: var(--white); }
</style>
</head>
<body>
<main class="canvas">

  <section class="card card-front" aria-label="Vorderseite">
    <div class="wordmark">
      <span class="wordmark-square"></span>
      <span class="wordmark-name">Tobias Kellinger</span>
    </div>
    <p class="job-title">Personal Trainer</p>
  </section>

  <section class="card card-back" aria-label="Rückseite">
    <div class="photo-column"></div>
    <div class="portrait" role="img" aria-label="Schwarzweiß-Porträt des Trainers mit verschränkten Armen"></div>

    <div class="contact">
      <h1 class="contact-name">Tobias Kellinger</h1>
      <ul class="contact-list">
        <li>
          <svg viewBox="0 0 24 24"><path d="M2 5h20v14H2z M2 5l10 8 10-8" /><path d="M3 6l9 7 9-7" fill="none" stroke="#efefef" stroke-width="1.6"/></svg>
          t.kellinger@postfeld.de
        </li>
        <li>
          <svg viewBox="0 0 24 24"><path d="M6.6 10.8a15 15 0 0 0 6.6 6.6l2.2-2.2c.3-.3.7-.4 1-.2 1.1.4 2.3.6 3.6.6.6 0 1 .4 1 1V20c0 .6-.4 1-1 1A17 17 0 0 1 3 4c0-.6.4-1 1-1h3.5c.6 0 1 .4 1 1 0 1.3.2 2.5.6 3.6.1.3 0 .7-.2 1z"/></svg>
          0163/2918374
        </li>
        <li>
          <svg viewBox="0 0 24 24"><path d="M12 3l10 9h-3v8h-5v-6h-4v6H5v-8H2z"/></svg>
          Lindenfeldweg 14
        </li>
        <li class="address-line">80412 München</li>
      </ul>
    </div>

    <div class="footer-band">
      <span class="website">
        <svg viewBox="0 0 24 22" fill="none" stroke="#ffffff" stroke-width="2"><rect x="2" y="2" width="20" height="13" rx="1"/><path d="M8 20h8M12 15v5"/></svg>
        www.tobiaskellinger.de
      </span>
      <span class="band-wordmark"><span class="square"></span>Tobias Kellinger</span>
    </div>
  </section>

</main>
</body>
</html>
```